Funeral Services Site

We need a website for a Funeral Services company. The old website is: www.rouwcentrumkorvelaer.be We need the same structure and text.

Target Market(s)

Customers.

Coding

Coded - Design and coding required

Number of Pages Required

4 page

Font styles to use
Serif
Sans Serif
Script

```html
<!DOCTYPE html>
<html lang="nl">
<head>
<meta charset="utf-8">
<title>Rouwcentrum Korvelaer bvba</title>
<link rel="stylesheet" href="https://fonts.googleapis.com/css2?family=Roboto+Slab:wght@300;400;500;700&family=Noto+Serif:ital@1&family=Roboto:wght@300;400&display=swap">
<style>
:root{
  --ink:#111;
  --text:#333;
  --muted:#8a8a8a;
  --white:#fff;
  --paper:#f3f3f3;
  --dark:#0c0a09;
  --card:#0a0909;
  --line:#3a3634;
  --slab:"Roboto Slab", Georgia, serif;
  --ital:"Noto Serif", Georgia, serif;
  --sans:"Roboto", Arial, sans-serif;
}
*{box-sizing:border-box;margin:0;padding:0}
html,body{width:1200px;height:3437px;overflow:hidden}
body{position:relative;background:var(--white);font-family:var(--slab);color:var(--text)}
.abs{position:absolute}

/* header */
.site-header{position:absolute;left:0;top:0;width:1200px;height:96px;background:var(--white);z-index:3}
.brand{position:absolute;left:171px;top:22px;display:flex;align-items:center;gap:12px}
.brand-name{font:700 22px/24px var(--slab);color:var(--ink)}
.brand-mark{width:52px;height:52px;border:2px solid var(--ink);border-radius:50%}
.top-meta{position:absolute;right:174px;top:19px;font:400 13px var(--slab);color:var(--ink);display:flex;gap:28px}
.main-nav{position:absolute;right:174px;top:56px;display:flex;gap:34px;font:400 15.5px var(--slab);color:var(--ink)}

/* hero */
.hero{position:absolute;left:0;top:96px;width:1200px;height:580px;background:radial-gradient(ellipse at 55% 40%,#5c6a48 0%,#3b4330 40%,#1f2419 100%)}
.hero-title{position:absolute;top:255px;width:1200px;text-align:center;color:var(--white);font:500 34px var(--slab)}
.hero-sub{position:absolute;top:295px;width:1200px;text-align:center;color:var(--white);font:500 24px var(--slab)}
.hero-btn{position:absolute;left:485px;top:360px;width:230px;height:47px;border:2px solid var(--white);border-radius:24px;color:var(--white);font:400 19px/43px var(--slab);text-align:center}
.dots{position:absolute;top:556px;left:543px;display:flex;gap:6px}
.dots span{width:24px;height:4px;background:var(--white)}
.dots span.off{background:#9c9c9c}

/* about */
.about-title{left:171px;top:722px;font:500 32px var(--slab);color:var(--ink)}
.about-lead{left:171px;top:770px;width:440px;font:italic 19.5px/26px var(--ital);color:var(--ink)}
.about-text{left:171px;top:838px;width:430px;font:300 12.5px/19px var(--slab);color:var(--text)}
.about-text p+p{margin-top:19px}
.about-photo{left:670px;top:705px;width:370px;height:370px;border-radius:50%;background:linear-gradient(135deg,#e9e2d6 0%,#8a735c 45%,#2a211c 100%);border:4px solid var(--white);box-shadow:-8px 8px 0 0 var(--ink)}

/* services */
.services{position:absolute;left:0;top:1120px;width:1200px;height:690px;background:var(--dark)}
.services-title{top:1230px;width:1200px;text-align:center;color:var(--white);font:500 31px var(--slab)}
.card{position:absolute;top:1312px;width:275px;height:354px;border:1px solid var(--line);background:var(--card);text-align:center}
.card-photo{width:186px;height:186px;border-radius:50%;margin:24px auto 0;box-shadow:0 4px 10px rgba(255,255,255,.2)}
.card h3{margin-top:22px;font:400 20px var(--slab);color:var(--white)}
.card p{margin:10px auto 0;width:210px;font:300 11.5px/21px var(--slab);color:var(--muted)}

/* ceremony */
.ceremony-title{top:1836px;width:1200px;text-align:center;font:500 32px var(--slab);color:var(--ink)}
.ceremony-text{left:258px;top:1895px;width:684px;text-align:center;font:300 12.5px/23.5px var(--slab);color:var(--text)}
.rite{position:absolute;top:2044px;display:flex;align-items:center;gap:10px}
.rite svg{flex:none}
.rite span{font:400 16px/23px var(--slab);color:var(--text)}

/* gallery */
.gallery{position:absolute;left:0;top:2208px;width:1200px;height:376px;display:flex}
.gallery div{flex:1}

/* contact */
.contact{position:absolute;left:0;top:2584px;width:1200px;height:480px;background:var(--paper)}
.contact-title{top:2650px;width:1200px;text-align:center;font:500 32px var(--slab);color:var(--ink)}
.contact-text{left:290px;top:2705px;width:620px;text-align:center;font:300 12.5px/23px var(--slab);color:var(--text)}
.field{position:absolute;left:213px;width:382px;height:36px;background:var(--white);border:1px solid #d6d6d6;font:300 12px/34px var(--slab);padding-left:6px;color:var(--text)}
.field.msg{left:605px;width:382px;height:170px}
.submit{position:absolute;left:536px;top:2970px;width:123px;height:33px;background:var(--ink);border-radius:17px;color:var(--white);font:700 12px/33px var(--slab);text-align:center}
.bouquet{left:780px;top:2850px;width:415px;height:250px;border-radius:40% 20% 30% 40%;background:radial-gradient(ellipse at 50% 50%,#f4f1e6 0%,#cfd8b4 45%,rgba(80,100,50,.0) 75%)}

/* footer */
.site-footer{position:absolute;left:0;top:3030px;width:1200px;height:407px;background:var(--dark)}
.foot-col{position:absolute;top:3167px}
.foot-col h4{font:400 15px var(--slab);color:var(--white);margin-bottom:14px}
.foot-col li{list-style:none;font:300 11.5px/22px var(--slab);color:#9a9a9a}
.contact-row{display:flex;gap:18px;align-items:flex-start;margin-bottom:16px;font:300 11px/17px var(--sans);color:#9a9a9a}
.copyright{left:177px;top:3399px;font:400 11px var(--slab);color:var(--white)}
.social{position:absolute;top:3391px;left:942px;display:flex;gap:10px}
.social span{width:22px;height:22px;border-radius:50%;background:#2a2726;border:1px solid #555}
</style>
</head>
<body>

<header class="site-header">
  <div class="brand">
    <div class="brand-name">Rouwcentrum<br>Korvelaer bvba</div>
    <div class="brand-mark"></div>
  </div>
  <div class="top-meta"><span>Call:011 23 45 67</span><span>Nederlands ▾</span></div>
  <nav class="main-nav"><span>Home</span><span>Over ons</span><span>Online Condoleren</span><span>Bloemen bestellen</span><span>Contact</span></nav>
</header>

<section class="hero" role="img" aria-label="Witte rozen en groene bloemstukken op een kist"></section>
<div class="hero-title abs">Rouwcentrum Korvelaer bvba:</div>
<div class="hero-sub abs">een persoonlijke service in afscheidsbegeleiding</div>
<div class="hero-btn">Contacteer ons</div>
<div class="dots"><span></span><span class="off"></span><span></span><span></span></div>
<svg class="abs" style="left:0;top:600px" width="1200" height="80" viewBox="0 0 1200 80"><path d="M0 70 Q600 -50 1200 70 L1200 80 L0 80Z" fill="#fff"/></svg>

<h2 class="about-title abs">over ons</h2>
<div class="about-lead abs">Rouwcentrum Korvelaer, een complete service in rouw- en afscheidsbegeleiding</div>
<div class="about-text abs">
  <p>Afscheid nemen van een dierbare is één van de zwaarste dingen in een mensenleven. Rouwcentrum Korvelaer in Oosterveld neemt alle praktische en administratieve zaken die erbij komen kijken, voor u in handen. Zodat u in alle rust afscheid kunt nemen.</p>
  <p>Onze mensen hebben een ruime ervaring in afscheidsbegeleiding en staan 24 uur op 24 uur voor u klaar. Ons volledig gerenoveerde funerarium staat open voor u en uw kennissen, zodat u op elk moment van de dag uw dierbare kan groeten.</p>
</div>
<div class="about-photo abs" role="img" aria-label="Hand rustend op een kist met witte lelies"></div>

<section class="services" role="presentation"></section>
<svg class="abs" style="left:0;top:1120px" width="1200" height="50" viewBox="0 0 1200 50"><path d="M0 0 L1200 0 L1200 10 Q600 70 0 10Z" fill="#fff"/></svg>
<svg class="abs" style="left:0;top:1745px" width="1200" height="66" viewBox="0 0 1200 66"><path d="M0 50 Q600 -30 1200 50 L1200 66 L0 66Z" fill="#fff"/></svg>
<h2 class="services-title abs">What We Do</h2>
<div class="card" style="left:171px"><div class="card-photo" role="img" aria-label="Bloemstuk op een graf" style="background:radial-gradient(circle,#c05a7a,#3d5a3a 70%,#2a2a2a)"></div><h3>Sundm lorstena</h3><p>Sed ut perspiciatis unde omnis iste natus error sit voluptatem acsantium doloremque laudantiumotam</p></div>
<div class="card" style="left:462px"><div class="card-photo" role="img" aria-label="Kist met bloemen in een kerk" style="background:radial-gradient(circle,#d9c27a,#6b4a2c 60%,#241a14)"></div><h3>Sundm lorstena</h3><p>Sed ut perspiciatis unde omnis iste natus error sit voluptatem acsantium doloremque laudantiumotam</p></div>
<div class="card" style="left:752px"><div class="card-photo" role="img" aria-label="Boeket van rozen en lelies" style="background:radial-gradient(circle,#9aa6c8,#a03048 55%,#3a2a2a)"></div><h3>Sundm lorstena</h3><p>Sed ut perspiciatis unde omnis iste natus error sit voluptatem acsantium doloremque laudantiumotam</p></div>

<h2 class="ceremony-title abs">Organisatie uitvaart en eredienst</h2>
<p class="ceremony-text abs">De organisatie van de uitvaartplechtigheid is een moment van bezinning, waar de persoonlijkheid van de overledene mooi in de verf gezet kan worden. Ons team staat u hierin bij en selecteert met u de mooiste teksten, liederen en foto's om zo tot een gepast en waardig afscheid te komen. De uitvaart kan plaatsvinden in uw parochiekerk of onze aula als u dat wenst, die plaats biedt aan maximum 100 genodigden. We kunnen volgende zaken voor u regelen:</p>
<div class="rite" style="left:171px"><svg width="78" height="78" viewBox="0 0 78 78"><circle cx="39" cy="39" r="37" fill="none" stroke="#111" stroke-width="2"/><circle cx="39" cy="39" r="33" fill="none" stroke="#111" stroke-width="1"/><path d="M35 20h8v10h10v7H43v18h-8V37H25v-7h10Z" fill="none" stroke="#111" stroke-width="2"/><path d="M22 58h34" stroke="#111" stroke-width="2"/></svg><span>Gebedswake de avond<br>voor de begrafenis</span></div>
<div class="rite" style="left:475px"><svg width="78" height="78" viewBox="0 0 78 78"><circle cx="39" cy="39" r="37" fill="none" stroke="#111" stroke-width="2"/><circle cx="39" cy="39" r="33" fill="none" stroke="#111" stroke-width="1"/><path d="M37 18 L30 40 L22 52 L28 58 L37 48Z M41 18 L48 40 L56 52 L50 58 L41 48Z" fill="none" stroke="#111" stroke-width="2" stroke-linejoin="round"/></svg><span>Gebedsdienst met<br>priester (indien mogelijk)</span></div>
<div class="rite" style="left:798px"><svg width="78" height="78" viewBox="0 0 78 78"><circle cx="39" cy="39" r="37" fill="none" stroke="#111" stroke-width="2"/><circle cx="39" cy="39" r="33" fill="none" stroke="#111" stroke-width="1"/><path d="M26 22 Q39 30 52 22 Q54 42 39 46 Q24 42 26 22Z M39 46 V60" fill="none" stroke="#111" stroke-width="2"/></svg><span>Eucharistieviering<br>met priester</span></div>

<div class="gallery">
  <div role="img" aria-label="Witte orchideeën" style="background:linear-gradient(160deg,#3a3a28,#d8d2c0 50%,#5a6a3a)"></div>
  <div role="img" aria-label="Witte roos met groene bessen" style="background:linear-gradient(160deg,#4a6a2a,#e8e6cc 45%,#8aa64a)"></div>
  <div role="img" aria-label="Keramische rozen op staafjes" style="background:linear-gradient(90deg,#c8a888,#8a6a54 50%,#d8d0c8)"></div>
  <div role="img" aria-label="Kruis met witte bloemen" style="background:linear-gradient(180deg,#7a5a44,#3a2a20 60%,#1a1614)"></div>
</div>

<section class="contact"></section>
<h2 class="contact-title abs">Contact Us</h2>
<p class="contact-text abs">Sed ut perspiciatis unde omnis iste natus error sit voluptatem accusantium doloremque laudantium, totam rem aperiam, eaque ipsa quae Sed ut perspiciatis unde omnis iste natus error sit voluptatem</p>
<div class="field" style="top:2778px">Name:</div>
<div class="field" style="top:2823px">Email:</div>
<div class="field" style="top:2868px">Phone:</div>
<div class="field" style="top:2913px">Subject:</div>
<div class="field msg" style="top:2778px">Message:</div>
<div class="submit">SUBMIT</div>

<footer class="site-footer"></footer>
<svg class="abs" style="left:0;top:3025px" width="1200" height="70" viewBox="0 0 1200 70"><path d="M0 0 L1200 0 L1200 10 Q600 100 0 10Z" fill="#f3f3f3"/></svg>
<div class="bouquet abs" role="img" aria-label="Boeket witte lelies en groen"></div>

<div class="foot-col" style="left:170px">
  <h4>Contact</h4>
  <div class="contact-row"><svg width="18" height="22" viewBox="0 0 18 22"><path d="M9 21 C3 13 1 10 1 7 A8 8 0 0 1 17 7 C17 10 15 13 9 21Z" fill="none" stroke="#ccc" stroke-width="1.4"/><circle cx="9" cy="7" r="3" fill="none" stroke="#ccc" stroke-width="1.4"/></svg><span style="font-family:var(--slab)">Lindeweg 18<br>3700 Oosterveld</span></div>
  <div class="contact-row"><svg width="22" height="22" viewBox="0 0 22 22"><path d="M5 2 L9 6 L7 9 Q9 13 13 15 L16 13 L20 17 L17 20 Q8 19 2 5Z" fill="none" stroke="#ccc" stroke-width="1.4" stroke-linejoin="round"/></svg><span style="font-family:var(--slab)">24/24, 7 op 7<br>011 23 45 67</span></div>
  <div class="contact-row"><svg width="24" height="18" viewBox="0 0 24 18"><rect x="1" y="1" width="22" height="16" fill="none" stroke="#ccc" stroke-width="1.4"/><path d="M1 1 L12 10 L23 1" fill="none" stroke="#ccc" stroke-width="1.4"/></svg><span>E-mail:<br>info@rouwcentrumkorvelaer.be</span></div>
</div>
<div class="foot-col" style="left:474px"><h4>Flowers</h4><ul><li>Lorem ipsum dolo</li><li>Consectetur adcing elit.</li><li>Fusce eget leo tincid</li><li>Donec consequat</li><li>Praesent elementum</li><li>Jmauris posueret</li></ul></div>
<div class="foot-col" style="left:676px"><h4>Account</h4><ul><li>Lorem ipsum dolo</li><li>Consectetur adcing elit.</li><li>Fusce eget leo tincid</li><li>Donec consequat</li><li>Praesent elementum</li><li>Jmauris posueret</li></ul></div>
<div class="foot-col" style="left:883px"><h4>Other Links</h4><ul><li>Lorem ipsum dolo</li><li>Consectetur adcing elit.</li><li>Fusce eget leo tincid</li><li>Donec consequat</li><li>Praesent elementum</li><li>Jmauris posueret</li></ul></div>
<div class="copyright abs">Copyright 2019 All Rights Reserved.&nbsp; Sitemap - Privacy Policy</div>
<div class="social"><span></span><span></span><span></span></div>

</body>
</html>
```